Domestic Building Company requires professional webpage

We have an existing webpage that was never completed. We are a growing building company specialising in domestic building, renovations and commercial maintenance. We liaise closely with each of our clients to provide quality service they would be happy to recommend. Our easy approachable staff give our clients the confidence to discuss their needs and changes they may have along the way.
Our main source of new customers have been from recommendations of existing clients.
We would like our webpage to reflect our eye for detail and showcase our previous work.
The colour theme should be the same as the colours of our logo.
We would like the main page to really stand out with a slideshow of our pictures of works we have completed.
We would like the tabs to remain the same - Home, About Us, Our Services, Contact us.
In the Our Services section we would like each sub heading to be a link where viewers can see pictures from previous work we have completed.
Our current web page is www.ferncastconstruct.com.au

```html
<!DOCTYPE html>
<html lang="en">
<head>
<meta charset="utf-8">
<title>Ferncast Construct</title>
<link href="https://fonts.googleapis.com/css2?family=Open+Sans:wght@400;600&family=Varela+Round&display=swap" rel="stylesheet">
<style>
:root{
  --blue:#0a4f9e;
  --blue-dark:#063f85;
  --green:#7ac143;
  --green-dark:#5aa332;
  --text:#555;
  --muted:#888;
  --line:#e4e4e4;
}
*{margin:0;padding:0;box-sizing:border-box}
html,body{width:1042px;height:1200px;overflow:hidden;background:#fff}
body{font-family:"Open Sans",sans-serif;color:var(--text);position:relative}
.abs{position:absolute}
a{text-decoration:none;color:inherit}

/* header */
.site-header{position:absolute;left:0;top:0;width:1042px;height:118px;border-bottom:1px solid var(--line);background:#fff}
.brand{left:75px;top:30px;display:flex;align-items:center;gap:12px}
.brand-name{font-family:"Varela Round",sans-serif;font-size:38px;color:var(--blue);line-height:1}
.brand-mark{width:60px;height:60px;background:var(--green)}
.social{left:835px;top:32px;display:flex;gap:9px}
.social span{width:24px;height:24px;border-radius:3px;display:block}
.main-nav{left:424px;top:76px;display:flex;font-size:15px;font-weight:600;color:var(--blue)}
.main-nav a{position:absolute;white-space:nowrap;height:42px}
.main-nav a.active{color:var(--green)}
.main-nav a.active::after{content:"";position:absolute;left:-4px;right:-4px;bottom:0;height:6px;background:var(--green)}

/* hero */
.hero{left:0;top:118px;width:1042px;height:385px;background:linear-gradient(#eeeeee,#fff 18%,#fff 82%,#f0f0f0);border-bottom:1px solid #ddd}
.hero-title{left:77px;top:100px;font-family:"Varela Round",sans-serif;font-size:35px;color:var(--blue);white-space:nowrap}
.hero-sub{left:77px;top:143px;font-family:"Varela Round",sans-serif;font-size:27px;color:var(--green);white-space:nowrap}
.hero-text{left:78px;top:184px;font-size:12px;line-height:20px;color:#666;white-space:nowrap}
.dots{left:80px;top:236px;display:flex;gap:4px}
.dots span{width:12px;height:12px;border-radius:50%;background:#bbb}
.dots span:first-child{background:var(--blue)}
.hero-art{left:470px;top:12px;width:505px;height:340px;border-radius:6px;background:linear-gradient(160deg,#cfe0f4,#5d8fce 55%,#2f5e9e);opacity:.85}

/* welcome */
.welcome-title{left:74px;top:543px;font-family:"Varela Round",sans-serif;font-size:25.5px;color:var(--blue)}
.welcome-sub{left:74px;top:574px;font-size:15.5px;color:var(--blue)}
.welcome-body{left:71px;top:604px;width:565px;font-size:11px;line-height:19.3px}
.welcome-body p+p{margin-top:9px}
.btn{display:block;text-align:center;color:#fff;font-size:12.5px;font-weight:600;border-radius:3px;line-height:32px}
.btn-blue{left:72px;top:743px;width:109px;height:32px;background:linear-gradient(#1f6fc7,var(--blue-dark))}
.btn-green{left:408px;top:1023px;width:109px;height:31px;background:linear-gradient(#8fd25a,var(--green-dark));line-height:31px}

.old-projects{left:653px;top:544px;width:307px;height:236px;border-radius:3px;background:linear-gradient(#9ed66f,#68b43c);border:1px solid #5fa335}
.old-projects h2{position:absolute;left:23px;top:20px;font-family:"Varela Round",sans-serif;font-weight:400;font-size:24px;color:#fff}
.thumb{position:absolute;width:86px;height:72px;border:2px solid #fff;border-radius:3px}

/* columns */
.col-title{top:815px;font-family:"Open Sans",sans-serif;font-size:21px;color:#444}
.col-title.blue{color:var(--blue)}
.project{left:76px;width:300px;height:60px}
.project .pic{position:absolute;left:0;top:0;width:73px;height:57px}
.project h3{position:absolute;left:83px;top:-2px;font-size:13.5px;font-weight:400;color:#444}
.project p{position:absolute;left:84px;top:20px;font-size:10.5px;line-height:16px;color:var(--muted);width:220px}
.why{left:407px;top:848px;width:275px;font-size:10.8px;line-height:19.3px;color:#777}
.why p+p{margin-top:9px}
.services{left:708px;top:848px;width:253px;list-style:none;font-size:11.5px;color:#555}
.services li{height:31px;line-height:23px;padding-left:13px;position:relative;border-bottom:1px solid #eee;white-space:nowrap}
.services li:last-child{border-bottom:none}
.services li::before{content:"";position:absolute;left:1px;top:8px;border-left:4px solid #bbb;border-top:4px solid transparent;border-bottom:4px solid transparent}

/* footer */
.site-footer{left:0;top:1104px;width:1042px;height:96px;background:linear-gradient(#1e6cc3,#0a4595)}
.footer-nav{left:78px;top:22px;font-size:13.5px;font-weight:600;color:#e6eefa;white-space:nowrap}
.footer-nav span{margin:0 8px;color:#9fbce6;font-weight:400}
.copyright{left:78px;top:48px;font-size:11.5px;color:#7ea6dc}
</style>
</head>
<body>

<header class="site-header">
  <div class="abs brand"><span class="brand-name">ferncast</span><span class="brand-mark"></span></div>
  <div class="abs social" aria-label="Social links">
    <span style="background:#3b5b9a"></span><span style="background:#35b6e8"></span><span style="background:#1d74b0"></span><span style="background:#f48a1d"></span>
  </div>
  <nav class="abs main-nav">
    <a class="active" style="left:0">HOME</a>
    <a style="left:73px">ABOUT US</a>
    <a style="left:174px">OUR SERVICES</a>
    <a style="left:310px">OUR PROJECTS</a>
    <a style="left:445px">CONTACT US</a>
  </nav>
</header>

<section class="abs hero">
  <div class="abs hero-art" role="img" aria-label="Slideshow image: cluster of glass office towers"></div>
  <h1 class="abs hero-title" style="font-weight:400">Construction &amp; Building</h1>
  <div class="abs hero-sub">Phasellus felis dolor scelerisque</div>
  <p class="abs hero-text">Morbi diam mauris viverra in gravida eu mattis in ante Morbi eget arcu<br>Morbi porta libero id ullamcorper nonummy nibh ligula pulvinar</p>
  <div class="abs dots"><span></span><span></span><span></span><span></span></div>
</section>

<h2 class="abs welcome-title" style="font-weight:400">Welcome to Our Website Mainpage</h2>
<div class="abs welcome-sub">Mauris nunc quam venenatis nec euismod sit amet&nbsp; egestas placerat est</div>
<div class="abs welcome-body">
  <p>Ferncast Construct Pty Ltd is a construction and renovation company that is based in the Illawarra area.&nbsp; We specialise in all areas of residential and commercial building works and aim to deliver the highest quality performance at an affordable price. We ensure our workers have undergone the qualifications and training to provide the workmanship, efficiency and reliability our clients expect.</p>
  <p>We actively engage our client from the initial greeting to the finished product, we achieve this by ensuring the clients needs remain our first priority when delivering a high quality service and product.</p>
</div>
<a class="abs btn btn-blue">READ MORE</a>

<aside class="abs old-projects">
  <h2>Old Projects</h2>
  <div class="thumb" style="left:21px;top:52px;background:linear-gradient(135deg,#6d6d6d,#2d2d2d)" role="img" aria-label="Project photo: interior staircase"></div>
  <div class="thumb" style="left:112px;top:52px;background:linear-gradient(#8a9a7a,#5c6b3a)" role="img" aria-label="Project photo: timber gazebo on lawn"></div>
  <div class="thumb" style="left:204px;top:52px;background:linear-gradient(90deg,#8d9090,#5fc9b5)" role="img" aria-label="Project photo: rendered wall with door"></div>
  <div class="thumb" style="left:21px;top:132px;background:linear-gradient(135deg,#5a4a3a,#1f1f1f)" role="img" aria-label="Project photo: interior doorway"></div>
  <div class="thumb" style="left:112px;top:132px;background:linear-gradient(#6e7a86,#3f4650)" role="img" aria-label="Project photo: slatted fence"></div>
  <div class="thumb" style="left:204px;top:132px;background:linear-gradient(#6a6a6a,#1c2440)" role="img" aria-label="Project photo: bedroom"></div>
</aside>

<h2 class="abs col-title" style="left:76px;font-weight:400">Latest Projects</h2>
<div class="abs project" style="top:853px">
  <div class="pic" style="background:linear-gradient(#7a6a5a,#3a3330)" role="img" aria-label="Project photo: living room"></div>
  <h3>Etiam est nunc venenatis</h3>
  <p>Class aptent taciti sociosqu ad litora torquent per conubia nostra, per inceptos</p>
</div>
<div class="abs project" style="top:926px">
  <div class="pic" style="background:linear-gradient(#6a4a30,#2e2116)" role="img" aria-label="Project photo: timber screen"></div>
  <h3>Mauris neque metus</h3>
  <p>Class aptent taciti sociosqu ad litora torquent per conubia nostra hymenaeos</p>
</div>
<div class="abs project" style="top:998px">
  <div class="pic" style="background:linear-gradient(#5a5048,#d8d8d8)" role="img" aria-label="Project photo: bathroom spa"></div>
  <h3>Curabitur iaculis</h3>
  <p>Class aptent taciti sociosqu per conubia nostra, per inceptos hymenaeos</p>
</div>

<h2 class="abs col-title" style="left:406px;font-weight:400">Why Choose Us</h2>
<div class="abs why">
  <p>Aliquam nec erat at purus cursus interdum Vestibulum ligula augue bibendum accumsan vestibulum ut commodo a mi Morbi ornare gravida elit Integer congue augue et malesuada iaculis ipsum dui aliquet felis at cursus magna nisl nec elit</p>
  <p>Vestibulum gravida Praesent elementum elit at tellus Malesuada nec ultricies sit ametporttitor mattis enim In massa libero interdum nec</p>
</div>
<a class="abs btn btn-green">READ MORE</a>

<h2 class="abs col-title blue" style="left:706px;font-weight:400">Services We Provide</h2>
<ul class="abs services">
  <li>Etiam eu urna Sed porta Suspendisse</li>
  <li>Quam leo molestie sed luctus quis feugiat</li>
  <li>Fusce tellus Sed metus augue convallis</li>
  <li>Et vehicula ut pulvinar eu ante Integer</li>
  <li>Eristique vitae consequat nec porta vel lectus</li>
  <li>Nulla sit amet diam Duis non nunc</li>
</ul>

<footer class="abs site-footer">
  <div class="abs footer-nav">Home<span>|</span>About us<span>|</span>Millwork projects<span>|</span>House designs<span>|</span>Contact us</div>
  <div class="abs copyright">Copyright © 2013 Company Name.&nbsp; All right reseved</div>
</footer>

</body>
</html>
```